Catalogue design for construction materials supplies

We need to design a new product catalogue for building material supply company based in Singapore called "Toh Besar Supplies Pte Ltd" . We supply a wide range of construction related materials in the local market and is one of the leading stockist of construction material in Singapore. We would like the design to be modern and industrial showing green sustainable building.
Updates

Project Deadline Extended
Reason: I would not be able to consolidate for my supervisor to decide on the design as I will be away for business trip the next 4 days. My Apologies.

Target Market(s)

Developers, Main Constructors, Sub Contractors, Construction company

Industry/Entity Type

Construction

Font styles to use
Serif

Colors
0255a3
ffc214
ec1f27
85acd3
abd037
9bcb3b
3276b5
fbed22
f37122

Requirements
Must have
• Company Logo, awards logo, product pictures

```html
<!DOCTYPE html>
<html lang="en">
<head>
<meta charset="utf-8">
<title>Clay Block Catalogue Spread</title>
<link href="https://fonts.googleapis.com/css2?family=Montserrat:wght@700&family=Roboto:wght@400;500;700&display=swap" rel="stylesheet">
<style>
  :root {
    --brand-blue: #2b4f9e;
    --brand-red: #d7252f;
    --ink: #2a1f33;
    --spec-ink: #333333;
    --frame: #e2e2e2;
    --page: #ffffff;
    --page-shade: #f3f3f3;
    --backdrop: #d6d4cf;
    --clay-light: #a8744a;
    --clay-mid: #8a5a36;
    --clay-dark: #6a4026;
  }
  * { box-sizing: border-box; margin: 0; padding: 0; }
  html, body { width: 1200px; height: 804px; overflow: hidden; }
  body {
    background: var(--backdrop);
    font-family: "Roboto", Arial, sans-serif;
    position: relative;
  }
  .spread {
    position: absolute;
    left: 30px; top: 17px;
    width: 1140px; height: 770px;
    display: flex;
    box-shadow: 0 6px 20px rgba(0,0,0,0.18);
  }
  .page {
    position: relative;
    width: 570px; height: 770px;
    background: var(--page);
    overflow: hidden;
  }
  .page--left { background: linear-gradient(90deg, var(--page) 88%, var(--page-shade)); }
  .page--right { background: linear-gradient(90deg, var(--page-shade), var(--page) 12%); }
  .page-title {
    font-family: "Montserrat", Arial, sans-serif;
    font-weight: 700;
    font-size: 30px;
    color: var(--ink);
    text-align: center;
    padding-top: 38px;
    height: 100px;
  }
  .product-grid {
    display: grid;
    grid-template-columns: repeat(3, 150px);
    column-gap: 16px;
    row-gap: 22px;
    justify-content: center;
  }
  .product-card { width: 150px; }
  .product-photo {
    height: 118px;
    border: 1px solid var(--frame);
    background: #fff;
    padding: 14px 22px 20px;
  }
  .product-photo-fill {
    width: 100%; height: 100%;
    background: linear-gradient(160deg, var(--clay-light), var(--clay-mid) 55%, var(--clay-dark));
  }
  .product-label {
    background: var(--brand-red);
    color: #fff;
    font-size: 11px;
    font-weight: 500;
    height: 26px;
    line-height: 26px;
    padding-left: 9px;
    margin: -6px 0 0 -6px;
    width: 142px;
    white-space: nowrap;
  }
  .product-specs {
    font-size: 6.5px;
    color: var(--spec-ink);
    line-height: 9px;
    padding: 5px 0 4px 6px;
    border-bottom: 1.5px solid var(--brand-blue);
  }
  .product-specs b { font-weight: 700; }
  .page-footer {
    position: absolute;
    left: 0; bottom: 0;
    width: 570px; height: 70px;
  }
  .footer-name {
    position: absolute;
    bottom: 10px;
    color: #fff;
    font-size: 11px;
    letter-spacing: 0.3px;
  }
  .page--left .footer-name { left: 80px; }
  .page--right .footer-name { right: 70px; }
  .page-number {
    position: absolute;
    bottom: 50px;
    color: #fff;
    font-size: 11px;
    font-weight: 700;
  }
  .page--left .page-number { right: 10px; }
  .page--right .page-number { left: 10px; }
</style>
</head>
<body>
<div class="spread">

  <section class="page page--left">
    <h2 class="page-title">Clay Block</h2>
    <div class="product-grid">
      <article class="product-card"><div class="product-photo"><div class="product-photo-fill" role="img" aria-label="Photo of a 10 holes clay block"></div></div><div class="product-label">10 Holes Clay Block (KL)</div><p class="product-specs"><b>Product Size :</b> 215 x 100 x 135 mm<br><b>Product Packing :</b> 384 pcs/plt 9 plts/Load</p></article>
      <article class="product-card"><div class="product-photo"><div class="product-photo-fill" role="img" aria-label="Photo of a 10 holes clay block"></div></div><div class="product-label">10 Holes Clay Block (KL)</div><p class="product-specs"><b>Product Size :</b> 215 x 100 x 135 mm<br><b>Product Packing :</b> 384 pcs/plt 9 plts/Load</p></article>
      <article class="product-card"><div class="product-photo"><div class="product-photo-fill" role="img" aria-label="Photo of a 10 holes clay block"></div></div><div class="product-label">10 Holes Clay Block (KL)</div><p class="product-specs"><b>Product Size :</b> 215 x 100 x 135 mm<br><b>Product Packing :</b> 384 pcs/plt 9 plts/Load</p></article>
      <article class="product-card"><div class="product-photo"><div class="product-photo-fill" role="img" aria-label="Photo of a 10 holes clay block"></div></div><div class="product-label">10 Holes Clay Block (KL)</div><p class="product-specs"><b>Product Size :</b> 215 x 100 x 135 mm<br><b>Product Packing :</b> 384 pcs/plt 9 plts/Load</p></article>
      <article class="product-card"><div class="product-photo"><div class="product-photo-fill" role="img" aria-label="Photo of a 10 holes clay block"></div></div><div class="product-label">10 Holes Clay Block (KL)</div><p class="product-specs"><b>Product Size :</b> 215 x 100 x 135 mm<br><b>Product Packing :</b> 384 pcs/plt 9 plts/Load</p></article>
      <article class="product-card"><div class="product-photo"><div class="product-photo-fill" role="img" aria-label="Photo of a 10 holes clay block"></div></div><div class="product-label">10 Holes Clay Block (KL)</div><p class="product-specs"><b>Product Size :</b> 215 x 100 x 135 mm<br><b>Product Packing :</b> 384 pcs/plt 9 plts/Load</p></article>
      <article class="product-card"><div class="product-photo"><div class="product-photo-fill" role="img" aria-label="Photo of a 10 holes clay block"></div></div><div class="product-label">10 Holes Clay Block (KL)</div><p class="product-specs"><b>Product Size :</b> 215 x 100 x 135 mm<br><b>Product Packing :</b> 384 pcs/plt 9 plts/Load</p></article>
      <article class="product-card"><div class="product-photo"><div class="product-photo-fill" role="img" aria-label="Photo of a 10 holes clay block"></div></div><div class="product-label">10 Holes Clay Block (KL)</div><p class="product-specs"><b>Product Size :</b> 215 x 100 x 135 mm<br><b>Product Packing :</b> 384 pcs/plt 9 plts/Load</p></article>
      <article class="product-card"><div class="product-photo"><div class="product-photo-fill" role="img" aria-label="Photo of a 10 holes clay block"></div></div><div class="product-label">10 Holes Clay Block (KL)</div><p class="product-specs"><b>Product Size :</b> 215 x 100 x 135 mm<br><b>Product Packing :</b> 384 pcs/plt 9 plts/Load</p></article>
    </div>
    <svg class="page-footer" viewBox="0 0 570 70" aria-hidden="true">
      <path d="M420 30 L570 0 L570 40 Z" fill="var(--brand-red)"/>
      <path d="M0 40 L570 22 L570 70 L0 70 Z" fill="var(--brand-blue)"/>
    </svg>
    <span class="footer-name">Toh Besar Supplies Pte Ltd.</span>
    <span class="page-number">02</span>
  </section>

  <section class="page page--right">
    <h2 class="page-title">Clay Block</h2>
    <div class="product-grid">
      <article class="product-card"><div class="product-photo"><div class="product-photo-fill" role="img" aria-label="Photo of a 10 holes clay block"></div></div><div class="product-label">10 Holes Clay Block (KL)</div><p class="product-specs"><b>Product Size :</b> 215 x 100 x 135 mm<br><b>Product Packing :</b> 384 pcs/plt 9 plts/Load</p></article>
      <article class="product-card"><div class="product-photo"><div class="product-photo-fill" role="img" aria-label="Photo of a 10 holes clay block"></div></div><div class="product-label">10 Holes Clay Block (KL)</div><p class="product-specs"><b>Product Size :</b> 215 x 100 x 135 mm<br><b>Product Packing :</b> 384 pcs/plt 9 plts/Load</p></article>
      <article class="product-card"><div class="product-photo"><div class="product-photo-fill" role="img" aria-label="Photo of a 10 holes clay block"></div></div><div class="product-label">10 Holes Clay Block (KL)</div><p class="product-specs"><b>Product Size :</b> 215 x 100 x 135 mm<br><b>Product Packing :</b> 384 pcs/plt 9 plts/Load</p></article>
      <article class="product-card"><div class="product-photo"><div class="product-photo-fill" role="img" aria-label="Photo of a 10 holes clay block"></div></div><div class="product-label">10 Holes Clay Block (KL)</div><p class="product-specs"><b>Product Size :</b> 215 x 100 x 135 mm<br><b>Product Packing :</b> 384 pcs/plt 9 plts/Load</p></article>
      <article class="product-card"><div class="product-photo"><div class="product-photo-fill" role="img" aria-label="Photo of a 10 holes clay block"></div></div><div class="product-label">10 Holes Clay Block (KL)</div><p class="product-specs"><b>Product Size :</b> 215 x 100 x 135 mm<br><b>Product Packing :</b> 384 pcs/plt 9 plts/Load</p></article>
      <article class="product-card"><div class="product-photo"><div class="product-photo-fill" role="img" aria-label="Photo of a 10 holes clay block"></div></div><div class="product-label">10 Holes Clay Block (KL)</div><p class="product-specs"><b>Product Size :</b> 215 x 100 x 135 mm<br><b>Product Packing :</b> 384 pcs/plt 9 plts/Load</p></article>
      <article class="product-card"><div class="product-photo"><div class="product-photo-fill" role="img" aria-label="Photo of a 10 holes clay block"></div></div><div class="product-label">10 Holes Clay Block (KL)</div><p class="product-specs"><b>Product Size :</b> 215 x 100 x 135 mm<br><b>Product Packing :</b> 384 pcs/plt 9 plts/Load</p></article>
      <article class="product-card"><div class="product-photo"><div class="product-photo-fill" role="img" aria-label="Photo of a 10 holes clay block"></div></div><div class="product-label">10 Holes Clay Block (KL)</div><p class="product-specs"><b>Product Size :</b> 215 x 100 x 135 mm<br><b>Product Packing :</b> 384 pcs/plt 9 plts/Load</p></article>
      <article class="product-card"><div class="product-photo"><div class="product-photo-fill" role="img" aria-label="Photo of a 10 holes clay block"></div></div><div class="product-label">10 Holes Clay Block (KL)</div><p class="product-specs"><b>Product Size :</b> 215 x 100 x 135 mm<br><b>Product Packing :</b> 384 pcs/plt 9 plts/Load</p></article>
    </div>
    <svg class="page-footer" viewBox="0 0 570 70" aria-hidden="true">
      <path d="M0 0 L150 30 L0 40 Z" fill="var(--brand-red)"/>
      <path d="M0 24 L570 40 L570 70 L0 70 Z" fill="var(--brand-blue)"/>
    </svg>
    <span class="page-number">02</span>
    <span class="footer-name">Toh Besar Supplies Pte Ltd.</span>
  </section>

</div>
</body>
</html>
```